Wordpress Design for brand building and advertising company

I would like something with great looking colors to match a logo as well and, call to action buttons. Needs to be mobile ready. I also need to be able to upload site to web hosting provider. This website will be about helping small business build a brand. I would like something built that would show that we are serious about what we do and look to improve someone business with our services.

Target Market(s)

Small business looking to build a brand.

Industry/Entity Type

Digital Marketing

Logo Text

Qelvosta

Font styles to use
Sans Serif

Colors

Designer to choose colors to be used in the design.

Requirements
Must have
• Call to action with contact form.
• mobile ready
• favicon
• Easy word press upload.
• design best practices
• -Home
• -About
• -Services
• - Contact Us
• - Privacy/Terms
• My site: qelvosta.com
Nice to have
• Content ( can make ti better )
• Feed back on how to rank better.
Should not have
• Image here on website with no picture
• poor looking design,.

```html
<!DOCTYPE html>
<html lang="en">
<head>
<meta charset="utf-8">
<title>Qelvosta — Creating Strategies For Measurable Results</title>
<link href="https://fonts.googleapis.com/css2?family=Libre+Baskerville&family=Lato:wght@400;700&display=swap" rel="stylesheet">
<style>
:root{
  --orange:#f7810f;
  --orange-deep:#e86d10;
  --purple:#2c1a5c;
  --purple-deep:#2a0f5e;
  --ink:#1e1e2a;
  --text:#333;
  --bg:#f6f6f6;
  --white:#fff;
  --sky:#b8cfe0;
  --peach:#f6c89a;
}
*{box-sizing:border-box;margin:0;padding:0}
html,body{width:1200px;height:3025px;overflow:hidden}
body{background:var(--bg);font-family:'Lato',sans-serif;color:var(--text);position:relative}
.serif{font-family:'Libre Baskerville',serif}
.backdrop{position:absolute;left:0;top:0;width:1200px;height:3025px}
.abs{position:absolute}

/* header */
.site-header{position:absolute;left:0;top:0;width:1200px;height:110px;background:var(--white)}
.brand{position:absolute;left:80px;top:36px;display:flex;align-items:center;gap:10px;font-family:'Libre Baskerville',serif;font-size:30px;color:var(--purple)}
.brand-dot{width:16px;height:16px;border-radius:50%;background:var(--orange)}
.main-nav{position:absolute;left:495px;top:44px;display:flex;gap:38px;font-size:14px;color:#333}
.main-nav .active{color:#1f4e8c;border-bottom:2px solid #1f4e8c;padding-bottom:4px}
.btn-quote{position:absolute;left:990px;top:38px;width:128px;height:32px;border-radius:8px;background:var(--purple);color:#fff;font-size:13px;font-weight:700;display:flex;align-items:center;justify-content:center}

/* hero */
.hero-title{left:125px;top:278px;color:#fff;font-size:33px;line-height:44px}
.btn{display:flex;align-items:center;justify-content:center;background:var(--orange);color:#fff;border-radius:20px;font-size:15px}
.hero-btn{left:124px;top:376px;width:138px;height:34px}
.hero-art{left:520px;top:140px;width:650px;height:590px;border-radius:40px;background:radial-gradient(circle at 55% 40%,#e9ecf2 0,#c8d0e6 35%,rgba(240,140,60,.0) 70%)}

/* sections */
.section-title{left:0;width:1200px;text-align:center;color:var(--ink);font-size:33px}
.section-text{left:0;width:1200px;text-align:center;font-size:13px;line-height:18px;color:#333}
.about-btn{left:520px;top:940px;width:160px;height:38px}

.card{position:absolute;width:318px;height:330px;background:#fff;border-radius:20px;text-align:center;color:#333}
.card.featured{background:var(--purple);color:#fff}
.card-icon{width:106px;height:106px;border-radius:50%;background:var(--purple);margin:34px auto 0;display:flex;align-items:center;justify-content:center}
.card.featured .card-icon{background:var(--orange)}
.card h3{font-family:'Libre Baskerville',serif;font-weight:400;font-size:17px;line-height:22px;margin-top:26px;min-height:44px}
.card p{font-size:12px;line-height:16px;margin-top:8px}
.card .more{display:inline-block;margin-top:18px;font-size:12px;border-bottom:1px solid currentColor}

/* testimonials */
.avatar{position:absolute;border-radius:50%}
.avatar.side{width:122px;height:122px;top:2056px;background:linear-gradient(140deg,#8a8078,#cfc2b5);border:4px solid #fff}
.avatar.main{left:510px;top:2030px;width:162px;height:162px;background:linear-gradient(140deg,#c08040,#7a4a2a);border:5px solid #fff;box-shadow:0 4px 14px rgba(0,0,0,.15)}
.arrow{position:absolute;top:2110px;width:20px;height:20px;border:1.5px solid #333;border-radius:50%;display:flex;align-items:center;justify-content:center}
.stars{left:0;width:1200px;top:2322px;text-align:center;color:#f5a21b;font-size:15px;letter-spacing:3px}
.dots{left:580px;top:2348px;display:flex;gap:6px}
.dots span{width:6px;height:6px;border-radius:50%;background:#ccc}
.dots span:first-child{background:var(--purple)}

/* footer */
.news-title{left:0;width:1200px;top:2585px;text-align:center;color:#fff;font-size:26px}
.news-input{left:315px;top:2641px;width:422px;height:38px;background:#fff;border-radius:20px;padding-left:52px;line-height:38px;font-size:13px;color:#999;font-style:italic}
.news-btn{left:745px;top:2641px;width:152px;height:38px}
.foot-brand{left:80px;top:2718px;color:#fff;font-family:'Libre Baskerville',serif;font-size:30px}
.foot-col{color:#fff;font-size:12px;line-height:26px}
.foot-col h4{font-family:'Libre Baskerville',serif;font-weight:400;font-size:17px;margin-bottom:10px}
.foot-col ul{list-style:disc;padding-left:18px}
.addr-line{display:flex;gap:10px;align-items:center;line-height:24px}
.field{position:absolute;height:28px;background:rgba(255,255,255,.18);color:#fff;font-size:12px;padding:5px 10px}
.copyright-bar{left:0;top:2975px;width:1200px;height:50px;background:var(--orange)}
.copyright{left:80px;top:2992px;color:#fff;font-size:12px}
.social{display:flex;gap:10px;left:930px;top:2986px}
.social span{width:28px;height:28px;border-radius:50%;background:#fff}
</style>
</head>
<body>

<svg class="backdrop" viewBox="0 0 1200 3025" aria-hidden="true">
  <defs>
    <linearGradient id="heroGrad" x1="0" y1="0" x2="0" y2="1">
      <stop offset="0" stop-color="#ef7a12"/>
      <stop offset=".55" stop-color="#b4421f"/>
      <stop offset="1" stop-color="#2a0f5e"/>
    </linearGradient>
    <linearGradient id="footGrad" x1="0" y1="0" x2="0" y2="1">
      <stop offset="0" stop-color="#f7810f"/>
      <stop offset=".45" stop-color="#d85a22"/>
      <stop offset="1" stop-color="#2a0f5e"/>
    </linearGradient>
  </defs>
  <path d="M0 110H1200V822C1040 815 900 770 770 700C620 620 470 580 330 470C230 400 110 405 0 440Z" fill="url(#heroGrad)"/>
  <path d="M40 440C170 430 280 500 400 620C320 540 200 460 40 440Z" fill="var(--sky)"/>
  <path d="M780 700C880 760 960 790 1040 820C940 800 860 770 780 700Z" fill="var(--peach)"/>
  <path d="M0 2340C130 2305 260 2320 390 2410C530 2505 710 2560 900 2572C1050 2580 1150 2620 1200 2640V3025H0Z" fill="url(#footGrad)"/>
  <path d="M190 2330C320 2360 430 2420 520 2510C420 2440 310 2370 190 2330Z" fill="var(--peach)"/>
  <path d="M820 2520C920 2540 1020 2590 1110 2680C1030 2620 930 2560 820 2520Z" fill="var(--sky)"/>
</svg>

<header class="site-header">
  <div class="brand"><span class="brand-dot"></span>Qelvosta</div>
  <nav class="main-nav">
    <span class="active">Home</span><span>About</span><span>Services</span><span>Contact Us</span><span style="margin-left:6px">Privacy/Terms</span>
  </nav>
  <div class="btn-quote">Get A Quote</div>
</header>

<h1 class="abs hero-title serif" style="font-weight:400">Creating Strategies For<br>Measurable Results.</h1>
<div class="abs btn hero-btn">Read More</div>
<div class="abs hero-art" role="img" aria-label="Illustration of two marketers with a megaphone, analytics screen and smartphone"></div>

<h2 class="abs section-title serif" style="top:766px;font-weight:400">About us</h2>
<p class="abs section-text" style="top:822px">Established in 2013 by Marcus Delane, Qelvosta Inc., is a professional small business marketing<br>consulting services in Brookvale Ohio, focused on increasing company growth and profits. With 6<br>years in branding and marketing.</p>
<p class="abs section-text" style="top:882px">we have worked with several industry professionals and businesses across multiple indus<br>tries creating brand awareness and revenue growth.</p>
<div class="abs btn about-btn">Read More</div>

<h2 class="abs section-title serif" style="top:1040px;font-weight:400">Our Services</h2>
<p class="abs section-text" style="top:1082px">Lorem Ipsum simply dummy text the printing and typesetting<br>and dummy Ipsum is simply dummy text of the printing.</p>

<div class="card" style="left:95px;top:1160px">
  <div class="card-icon"><svg width="56" height="56" viewBox="0 0 56 56" fill="none" stroke="#fff" stroke-width="2"><circle cx="28" cy="28" r="22"/><circle cx="28" cy="28" r="14"/><circle cx="28" cy="28" r="6"/><path d="M28 28L48 8M42 8h6v6"/></svg></div>
  <h3>Branding Design<br>and Strategy</h3>
  <p>Lorem Ipsum is simply dummy<br>of the printing and typesetting</p>
  <span class="more">Read More</span>
</div>
<div class="card featured" style="left:440px;top:1160px">
  <div class="card-icon"><svg width="56" height="56" viewBox="0 0 56 56" fill="none" stroke="#fff" stroke-width="2"><path d="M28 12a12 12 0 0 0-7 22v6h14v-6a12 12 0 0 0-7-22z"/><path d="M22 44h12M24 48h8M28 4v3M12 12l2 2M44 12l-2 2M6 26h3M47 26h3"/></svg></div>
  <h3>Marketing Plan Development<br>and Implementation</h3>
  <p>Lorem Ipsum is simply dummy<br>of the printing and typesetting</p>
  <span class="more">Read More</span>
</div>
<div class="card" style="left:787px;top:1160px">
  <div class="card-icon"><svg width="56" height="56" viewBox="0 0 56 56" fill="none" stroke="#fff" stroke-width="2"><rect x="30" y="6" width="18" height="12" rx="2"/><path d="M34 12h10M26 20a10 10 0 1 0-8 18v8h14v-6h4v-8l-3-4"/></svg></div>
  <h3>Business<br>Consulting</h3>
  <p>Lorem Ipsum is simply dummy<br>of the printing and typesetting</p>
  <span class="more">Read More</span>
</div>
<div class="card" style="left:268px;top:1520px">
  <div class="card-icon"><svg width="56" height="56" viewBox="0 0 56 56" fill="none" stroke="#fff" stroke-width="2"><path d="M14 6h20l8 8v36H14z"/><path d="M34 6v8h8M20 20h16M20 26h16M20 32h10M32 38l6 6M28 44h6"/></svg></div>
  <h3>Story Telling</h3>
  <p>Lorem Ipsum is simply dummy<br>of the printing and typesetting<br>in the industry.</p>
  <span class="more">Read More</span>
</div>
<div class="card" style="left:618px;top:1520px">
  <div class="card-icon"><svg width="56" height="56" viewBox="0 0 56 56" fill="none" stroke="#fff" stroke-width="2"><path d="M8 24h8l24-12v32L16 32H8z"/><path d="M14 32l4 12h6l-3-12M46 22l6-3M46 28h6M46 34l6 3"/></svg></div>
  <h3>Advertising</h3>
  <p>Lorem Ipsum is simply dummy<br>of the printing and typesetting<br>in the industry.</p>
  <span class="more">Read More</span>
</div>

<h2 class="abs section-title serif" style="top:1938px;font-weight:400;font-size:29px">Testimonials</h2>
<p class="abs section-text" style="top:1992px;font-size:11px">Testimonials</p>
<div class="arrow" style="left:280px"><svg width="8" height="8" viewBox="0 0 8 8"><path d="M5 1L2 4l3 3" stroke="#333" fill="none" stroke-width="1.5"/></svg></div>
<div class="arrow" style="left:866px"><svg width="8" height="8" viewBox="0 0 8 8"><path d="M3 1l3 3-3 3" stroke="#333" fill="none" stroke-width="1.5"/></svg></div>
<div class="avatar side" style="left:352px" role="img" aria-label="Client portrait photo"></div>
<div class="avatar main" role="img" aria-label="Portrait photo of Lena Marlowe"></div>
<div class="avatar side" style="left:710px" role="img" aria-label="Client portrait photo"></div>
<p class="abs section-text serif" style="top:2215px;font-size:15px">Lena Marlowe</p>
<p class="abs section-text" style="top:2238px;color:var(--orange);font-size:13px">Creative Director</p>
<p class="abs section-text" style="top:2270px;font-size:12px;line-height:17px"><span style="font-size:22px;position:relative;top:-8px">“</span> Lorem Ipsum simply dummy text the printing and ypesetting industry<br>simply dummy Ipsum is simply dummy text of the printing. <span style="font-size:22px">”</span></p>
<div class="abs stars">★★★★★</div>
<div class="abs dots"><span></span><span></span><span></span></div>

<h2 class="abs news-title serif" style="font-weight:400">Join Our Newletter</h2>
<div class="abs news-input">Email Here</div>
<div class="abs btn news-btn" style="font-size:13px">Subscribe</div>

<div class="abs foot-brand">Qelvosta</div>
<p class="abs foot-col" style="left:80px;top:2766px;width:230px;line-height:17px">Lorem Ipsum is simply dummy text of the printing and typesetting Ads and in the industry.</p>
<p class="abs foot-col" style="left:80px;top:2844px">Read More &#9432;</p>

<div class="abs foot-col" style="left:368px;top:2720px">
  <h4>Quick Link</h4>
  <ul><li>Home</li><li>About us</li><li>Services</li><li>Testimonialst</li><li>Contact us</li><li>Privacy/Terms</li></ul>
</div>

<div class="abs foot-col" style="left:575px;top:2720px">
  <h4>Company address</h4>
  <div class="addr-line"><svg width="12" height="14" viewBox="0 0 12 14" fill="none" stroke="#fff"><path d="M6 13S1 8 1 5a5 5 0 0 1 10 0c0 3-5 8-5 8z"/><circle cx="6" cy="5" r="1.6"/></svg>Qelvosta, Inc</div>
  <div style="padding-left:22px;line-height:24px">4120 Harlow Avenue Suite 210<br>Brookvale, Ohio 44012</div>
  <div class="addr-line"><svg width="12" height="12" viewBox="0 0 12 12" fill="none" stroke="#fff"><path d="M2 1h3l1 3-2 1a7 7 0 0 0 3 3l1-2 3 1v3c-6 0-10-4-9-9z"/></svg># 1 - (555) 310-7724</div>
  <div class="addr-line"><svg width="12" height="12" viewBox="0 0 12 12" fill="none" stroke="#fff"><rect x="1" y="3" width="10" height="8" rx="1"/><path d="M3 3V1h6v2"/></svg>1-(555) 602-1193</div>
  <div class="addr-line"><svg width="12" height="12" viewBox="0 0 12 12" fill="none" stroke="#fff"><rect x="1" y="1" width="10" height="10" rx="2"/><path d="M4 4h4M4 7h4"/></svg># (555)418-2067</div>
  <div class="addr-line"><svg width="12" height="10" viewBox="0 0 12 10" fill="none" stroke="#fff"><rect x="1" y="1" width="10" height="8"/><path d="M1 1l5 4 5-4"/></svg>info@qelvosta.com</div>
</div>

<div class="abs foot-col" style="left:828px;top:2716px"><h4>Contact us</h4></div>
<div class="field" style="left:828px;top:2755px;width:96px">Name</div>
<div class="field" style="left:930px;top:2755px;width:90px">Email</div>
<div class="field" style="left:1026px;top:2755px;width:94px">Phone</div>
<div class="field" style="left:828px;top:2790px;width:292px;height:70px">Message</div>
<div class="abs btn" style="left:828px;top:2878px;width:138px;height:36px;font-size:13px">Subscribe</div>

<div class="abs copyright-bar"></div>
<p class="abs copyright">CopyRight ©2019 Qelvosta. All Right Reserve</p>
<div class="abs social" aria-label="Social links"><span></span><span></span><span></span><span></span><span></span></div>

</body>
</html>
```